Technology Solutions Line Card

I need to create a one page line card that displays the services that my company provides and the certifications we hold.
Updates
I have an updated logo that I will post as soon as I get it later today. For now you can see an example at:
The new logo is very close to this and the colors are the same.
The file that I have posted is an example of what I think is a slick format. the upload is a two page document, but I really only like the first page. What I need a little bit of marketing and then room for the content that describes our core services and certifications.
The content of the line card needs to be divided into 9 categories:
Cloud (Virtual) Computing environments
Links are to our current brochures on these items for reference.
Greetings all,
Greetings everyone!
Target Market(s)
Small to Medium sized businesses as well as government institutions. This should be a one page "firm handshake" type exposure that tells the customer they are dealing with a first class professional operation.
Industry/Entity Type
It Company
Look and feel
Each slider illustrates characteristics of the customer's brand and the style your logo design should communicate.

```html
<!DOCTYPE html>
<html lang="en">
<head>
<meta charset="utf-8">
<title>Brightwave Systems – Line Card</title>
<link rel="stylesheet" href="https://fonts.googleapis.com/css2?family=Roboto+Condensed:wght@400;700&family=Arimo:wght@400;700&display=swap">
<style>
  :root {
    --orange: #f26a10;
    --ink: #1c1c1c;
    --frame-light: #e6e6e6;
    --paper: #ffffff;
  }
  * { margin: 0; padding: 0; box-sizing: border-box; }
  html, body { width: 1200px; height: 927px; overflow: hidden; background: var(--paper); }
  .card { position: relative; width: 1200px; height: 927px; background: var(--paper); font-family: "Arimo", Arial, sans-serif; color: var(--ink); }
  .frame, .connectors { position: absolute; left: 0; top: 0; }
  .brand { position: absolute; left: 36px; top: 34px; display: flex; align-items: center; gap: 18px; }
  .brand-mark { width: 70px; height: 66px; background: var(--orange); }
  .brand-text { display: flex; flex-direction: column; }
  .brand-name { font-family: "Roboto Condensed", Arial, sans-serif; font-weight: 700; font-size: 28px; line-height: 30px; color: var(--ink); letter-spacing: 0.5px; }
  .brand-tagline { font-family: "Roboto Condensed", Arial, sans-serif; font-weight: 700; font-size: 9.5px; letter-spacing: 0.6px; margin-top: 8px; text-align: right; color: var(--ink); }
  .services { position: absolute; left: 58px; top: 269px; list-style: none; }
  .service { display: flex; align-items: center; height: 48px; font-family: "Roboto Condensed", Arial, sans-serif; font-weight: 700; font-size: 18px; color: var(--ink); }
  .service svg { width: 32px; height: 32px; margin-right: 14px; flex: none; }
  .copy { position: absolute; left: 467px; width: 673px; font-size: 9.2px; line-height: 10.7px; text-align: justify; color: var(--ink); }
  .copy.accent { color: var(--orange); }
  .copy strong { font-weight: 700; }
  .website { position: absolute; right: 57px; top: 876px; font-family: "Arimo", Arial, sans-serif; font-weight: 700; font-size: 26px; color: var(--orange); }
</style>
</head>
<body>
<div class="card">

  <svg class="frame" width="1200" height="927" viewBox="0 0 1200 927" aria-hidden="true">
    <path d="M440 36 H1148 Q1155 36 1155 43 V828 H732 L705 885 H42 Q35 885 35 878 V150 Q35 143 42 143 H420 Z" fill="none" stroke="var(--frame-light)" stroke-width="1.5"/>
    <path d="M490 15 H1178 Q1185 15 1185 22 V855 H730 L702 912 H22 Q15 912 15 905 V127 Q15 120 22 120 H440 L490 15" fill="none" stroke="var(--orange)" stroke-width="2"/>
  </svg>

  <header class="brand">
    <div class="brand-mark"></div>
    <div class="brand-text">
      <span class="brand-name">BRIGHTWAVE SYSTEMS</span>
      <span class="brand-tagline">ENTERPRISE SOLUTIONS FOR EVERYONE</span>
    </div>
  </header>

  <svg class="connectors" width="1200" height="927" viewBox="0 0 1200 927" fill="none" stroke="var(--orange)" stroke-width="1.5" stroke-linejoin="round" aria-hidden="true">
    <path d="M230 293 H345 V170 H460"/>
    <path d="M337 342 H392 V286 H460"/>
    <path d="M405 389 H428 V350 H460"/>
    <path d="M250 437 H337 V467 H460"/>
    <path d="M246 485 H393 V571 H460"/>
    <path d="M205 533 H425 V626 H460"/>
    <path d="M156 629 H393 V684 H460"/>
    <path d="M266 677 H318 V741 H460"/>
    <g fill="var(--orange)" stroke="none">
      <circle cx="230" cy="293" r="3"/><circle cx="337" cy="342" r="3"/><circle cx="405" cy="389" r="3"/>
      <circle cx="250" cy="437" r="3"/><circle cx="246" cy="485" r="3"/><circle cx="205" cy="533" r="3"/>
      <circle cx="156" cy="629" r="3"/><circle cx="266" cy="677" r="3"/>
      <circle cx="460" cy="170" r="2"/><circle cx="460" cy="286" r="2"/><circle cx="460" cy="350" r="2"/>
      <circle cx="460" cy="467" r="2"/><circle cx="460" cy="571" r="2"/><circle cx="460" cy="626" r="2"/>
      <circle cx="460" cy="684" r="2"/><circle cx="460" cy="741" r="2"/>
    </g>
  </svg>

  <ul class="services">
    <li class="service">
      <svg viewBox="0 0 32 32" aria-hidden="true"><rect x="3" y="6" width="24" height="16" rx="2" fill="none" stroke="var(--orange)" stroke-width="3"/><rect x="11" y="22" width="8" height="4" fill="var(--orange)"/><rect x="7" y="26" width="16" height="3" fill="var(--orange)"/><path d="M22 2 L30 4 V10 Q30 15 22 17 Q16 15 16 10 V4 Z" fill="var(--orange)"/></svg>
      Outsourced IT
    </li>
    <li class="service">
      <svg viewBox="0 0 32 32" aria-hidden="true"><circle cx="16" cy="16" r="13" fill="none" stroke="var(--orange)" stroke-width="5"/><circle cx="16" cy="16" r="5" fill="none" stroke="var(--orange)" stroke-width="3"/></svg>
      Backup and Disaster Recovery
    </li>
    <li class="service">
      <svg viewBox="0 0 32 32" aria-hidden="true"><path d="M8 25 H25 A6 6 0 0 0 24 13 A8 8 0 0 0 9 14 A5.5 5.5 0 0 0 8 25 Z" fill="var(--orange)"/></svg>
      Cloud (Virtual) Computing environments
    </li>
    <li class="service">
      <svg viewBox="0 0 32 32" aria-hidden="true"><g fill="none" stroke="var(--orange)" stroke-width="3"><rect x="4" y="4" width="10" height="10"/><rect x="18" y="4" width="10" height="10"/><rect x="4" y="18" width="10" height="10"/><rect x="18" y="18" width="10" height="10"/></g></svg>
      Cloud Office Suite
    </li>
    <li class="service">
      <svg viewBox="0 0 32 32" aria-hidden="true"><path d="M16 2 L29 6 V15 Q29 25 16 30 Q3 25 3 15 V6 Z" fill="var(--orange)"/><rect x="11" y="14" width="10" height="8" fill="var(--paper)"/><path d="M13 14 V11 A3 3 0 0 1 19 11 V14" fill="none" stroke="var(--paper)" stroke-width="2"/></svg>
      Network Security
    </li>
    <li class="service">
      <svg viewBox="0 0 32 32" aria-hidden="true"><rect x="5" y="3" width="22" height="26" rx="2" fill="var(--orange)"/><circle cx="16" cy="14" r="6" fill="var(--paper)"/><circle cx="16" cy="14" r="2" fill="var(--orange)"/><rect x="9" y="23" width="7" height="2" fill="var(--paper)"/></svg>
      Server Care
    </li>
    <li class="service">
      <svg viewBox="0 0 32 32" aria-hidden="true"><rect x="3" y="5" width="26" height="18" rx="2" fill="var(--orange)"/><rect x="6" y="8" width="20" height="12" fill="var(--paper)"/><rect x="13" y="23" width="6" height="3" fill="var(--orange)"/><rect x="8" y="26" width="16" height="3" fill="var(--orange)"/></svg>
      Desktop and User Care
    </li>
    <li class="service">
      <svg viewBox="0 0 32 32" aria-hidden="true"><path d="M3 11 Q3 6 16 6 Q29 6 29 11 V13 H22 V10 H10 V13 H3 Z" fill="var(--orange)"/><path d="M8 14 H24 L28 27 H4 Z" fill="var(--orange)"/><g fill="var(--paper)"><circle cx="12" cy="18" r="1.3"/><circle cx="16" cy="18" r="1.3"/><circle cx="20" cy="18" r="1.3"/><circle cx="12" cy="22" r="1.3"/><circle cx="16" cy="22" r="1.3"/><circle cx="20" cy="22" r="1.3"/></g></svg>
      VOIP
    </li>
    <li class="service">
      <svg viewBox="0 0 32 32" aria-hidden="true"><circle cx="22" cy="10" r="7" fill="var(--orange)"/><circle cx="23" cy="9" r="2.5" fill="var(--paper)"/><path d="M17 14 L4 27 L7 30 L9 28 L11 30 L13 28 L11 26 L20 17 Z" fill="var(--orange)"/></svg>
      Vendor Management
    </li>
  </ul>

  <p class="copy" style="top:163px"><strong>Lorem ipsum dolor sit amet, consectetur adipiscing elit.</strong> Integer ipsum leo, posuere sodales tortor et, convallis ultrices dui. Fusce vulputate porttitor rutrum. Aenean ac lacus et erat euismod tempus. Nunc tincidunt, lectus sed fringilla laoreet, augue diam aliquam diam, quis vestibulum tellus ipsum sed arcu. Vivamus nibh leo, consectetur ut iaculis et, pulvinar sed enim. Aliquam ac velit sed neque euismod egestas. Nam tempor dolor sit amet placerat scelerisque. Pellentesque porta neque in posuere pellentesque.</p>

  <p class="copy" style="top:217px">Etiam auctor semper bibendum. Vivamus dapibus arcu id mi ornare, nec tempor nisi laoreet. Ut lorem dui, mattis et magna et, venenatis tempus enim. Vivamus fermentum lorem urna, a pulvinar leo dictum consequat. Nam sodales sapien non dapibus euismod. Mauris tellus ligula, consectetur ut libero ut, commodo iaculis sapien. Nullam ipsum magna, scelerisque id ultrices ac, condimentum in lectus. Proin aliquet, justo interdum aliquam tempor, enim metus imperdiet tellus, sed scelerisque sapien mi ut mi. Aliquam at lacinia ipsum. Aliquam a fringilla felis, vitae ultricies nisi.</p>

  <p class="copy accent" style="top:279px"><strong>Ipsum dolor sit amet, consectetur adipiscing elit.</strong> Integer ipsum leo, posuere sodales tortor et, convallis ultrices dui. Fusce vulputate porttitor rutrum. Aenean ac lacus et erat euismod tempus. Nunc tincidunt, lectus sed fringilla laoreet, augue diam aliquam diam, quis vestibulum tellus ipsum sed arcu. Vivamus nibh leo, consectetur ut iaculis et, pulvinar sed enim. Aliquam ac velit sed neque euismod egestas. Nam tempor dolor sit amet placerat scelerisque. Pellentesque porta neque in posuere pellentesque.</p>

  <p class="copy" style="top:346px">Etiam auctor semper bibendum. Vivamus dapibus arcu id mi ornare, nec tempor nisi laoreet. Ut lorem dui, mattis et magna et, venenatis tempus enim. Vivamus fermentum lorem urna, a pulvinar leo dictum consequat. Nam sodales sapien non dapibus euismod. Mauris tellus ligula, consectetur ut libero ut, commodo iaculis sapien. Nullam ipsum magna, scelerisque id ultrices ac, condimentum in lectus. Proin aliquet, justo interdum aliquam tempor, enim metus imperdiet tellus, sed scelerisque sapien mi ut mi. Aliquam at lacinia ipsum. Aliquam a fringilla felis, vitae ultricies nisi.</p>

  <p class="copy" style="top:398px">Lorem ipsum dolor sit amet, consectetur adipiscing elit. Integer ipsum leo, posuere sodales tortor et, convallis ultrices dui. Fusce vulputate porttitor rutrum. Aenean ac lacus et erat euismod tempus. Nunc tincidunt, lectus sed fringilla laoreet, augue diam aliquam diam, quis vestibulum tellus ipsum sed arcu. Vivamus nibh leo, consectetur ut iaculis et, pulvinar sed enim. Aliquam ac velit sed neque euismod egestas. Nam tempor dolor sit amet placerat scelerisque. Pellentesque porta neque in posuere pellentesque.</p>

  <p class="copy accent" style="top:462px">Etiam auctor semper bibendum. Vivamus dapibus arcu id mi ornare, nec tempor nisi laoreet. Ut lorem dui, mattis et magna et, venenatis tempus enim. Vivamus fermentum lorem urna, a pulvinar leo dictum consequat. Nam sodales sapien non dapibus euismod. Mauris tellus ligula, consectetur ut libero ut, commodo iaculis sapien. Nullam ipsum magna, scelerisque id ultrices ac, condimentum in lectus. Proin aliquet, justo interdum aliquam tempor, enim metus imperdiet tellus, sed scelerisque sapien mi ut mi. Aliquam at lacinia ipsum. Aliquam a fringilla felis, vitae ultricies nisi.</p>

  <p class="copy accent" style="top:516px">Lorem ipsum dolor sit amet, consectetur adipiscing elit. Integer ipsum leo, posuere sodales tortor et, convallis ultrices dui. Fusce vulputate porttitor rutrum. Aenean ac lacus et erat euismod tempus. Nunc tincidunt, lectus sed fringilla laoreet, augue diam aliquam diam, quis vestibulum tellus ipsum sed arcu. Vivamus nibh leo, consectetur ut iaculis et, pulvinar sed enim. Aliquam ac velit sed neque euismod egestas. Nam tempor dolor sit amet placerat scelerisque. Pellentesque porta neque in posuere pellentesque.</p>

  <p class="copy" style="top:566px">Lorem ipsum dolor sit amet, consectetur adipiscing elit. Integer ipsum leo, posuere sodales tortor et, convallis ultrices dui. Fusce vulputate porttitor rutrum. Aenean ac lacus et erat euismod tempus. Nunc tincidunt, lectus sed fringilla laoreet, augue diam aliquam diam, quis vestibulum tellus ipsum sed arcu. Vivamus nibh leo, consectetur ut iaculis et, pulvinar sed enim. Aliquam ac velit sed neque euismod egestas. Nam tempor dolor sit amet placerat scelerisque. Pellentesque porta neque in posuere pellentesque.</p>

  <p class="copy accent" style="top:621px">Etiam auctor semper bibendum. Vivamus dapibus arcu id mi ornare, nec tempor nisi laoreet. Ut lorem dui, mattis et magna et, venenatis tempus enim. Vivamus fermentum lorem urna, a pulvinar leo dictum consequat. Nam sodales sapien non dapibus euismod. Mauris tellus ligula, consectetur ut libero ut, commodo iaculis sapien. Nullam ipsum magna, scelerisque id ultrices ac, condimentum in lectus. Proin aliquet, justo interdum aliquam tempor, enim metus imperdiet tellus, sed scelerisque sapien mi ut mi. Aliquam at lacinia ipsum. Aliquam a fringilla felis, vitae ultricies nisi.</p>

  <p class="copy" style="top:681px">Lorem ipsum dolor sit amet, consectetur adipiscing elit. Integer ipsum leo, posuere sodales tortor et, convallis ultrices dui. Fusce vulputate porttitor rutrum. Aenean ac lacus et erat euismod tempus. Nunc tincidunt, lectus sed fringilla laoreet, augue diam aliquam diam, quis vestibulum tellus ipsum sed arcu. Vivamus nibh leo, consectetur ut iaculis et, pulvinar sed enim. Aliquam ac velit sed neque euismod egestas. Nam tempor dolor sit amet placerat scelerisque. Pellentesque porta neque in posuere pellentesque.</p>

  <p class="copy accent" style="top:736px">Etiam auctor semper bibendum. Vivamus dapibus arcu id mi ornare, nec tempor nisi laoreet. Ut lorem dui, mattis et magna et, venenatis tempus enim. Vivamus fermentum lorem urna, a pulvinar leo dictum consequat. Nam sodales sapien non dapibus euismod. Mauris tellus ligula, consectetur ut libero ut, commodo iaculis sapien. Nullam ipsum magna, scelerisque id ultrices ac, condimentum in lectus. Proin aliquet, justo interdum aliquam tempor, enim metus imperdiet tellus, sed scelerisque sapien mi ut mi. Aliquam at lacinia ipsum. Aliquam a fringilla felis, vitae ultricies nisi.<br>Lorem ipsum dolor sit amet, consectetur adipiscing elit. Integer ipsum leo, posuere sodales tortor et, convallis ultrices dui. Fusce vulputate porttitor rutrum. Aenean ac lacus et erat euismod tempus. Nunc tincidunt, lectus sed fringilla laoreet, augue diam aliquam diam, quis vestibulum tellus ipsum sed arcu. Vivamus nibh leo, consectetur ut iaculis et, pulvinar sed enim. Aliquam ac velit sed neque euismod egestas. Nam tempor dolor sit amet placerat scelerisque. Pellentesque porta neque in posuere pellentesque.</p>

  <p class="website">www.brightwavesystems.net</p>
</div>
</body>
</html>
```